StayCrewly.com homepage

We need a new homepage for our new domain.

StayCrewly.com

The colors to be used are the ones in our logo (attached) and in the current log in page host.nestarloo.com

Its important its a ONE PAGE site where you can scroll and elements appear while scrolling down.

It has to be simple to the point similar to the chatterloop log in page.

The current log in box and registration box have to stay but can be moved around obviously.

Also the video as on our current page www.nestarloo.com needs to have its place on the homepage.

Slogan

StayCrewly.com - The Booking Collaboration Platform.

Vacation rental managers and hosts can now team up with a booking team. Its easy to instantly improve your online booking management. Be on all the best booking sites without all the hassle. Improve your current strategy and save loads of time which you can spend on the satisfaction of your guests.

Something like that not too long.

I look forward to seeing your proposed designs.

In the attachment is our logo and a screenshot of our backend so the design will match nicely

Target Market(s)

Owners and property managers of vacation rentals world wide

Industry/Entity Type

Domain

Number of Pages Required

1 page

Requirements
Nice to have
• Smooth scrolling elements

```html
<!DOCTYPE html>
<html lang="en">
<head>
<meta charset="utf-8">
<title>StayCrewly.com – The Booking Collaboration Platform</title>
<link href="https://fonts.googleapis.com/css2?family=Ubuntu:wght@300;400;500;700&display=swap" rel="stylesheet">
<style>
  :root {
    --navy: #0b3a86;
    --navy-deep: #083581;
    --orange: #f55a16;
    --ink: #2a2a2a;
    --grey-text: #8a8a8a;
    --field-line: #cfcfcf;
    --login-grey: #5d5d5d;
    --partners-bg: #e9e9e9;
    --how-bg: #7aabd6;
    --footer-bg: #5a5a5a;
    --white: #ffffff;
  }
  * { box-sizing: border-box; margin: 0; padding: 0; }
  html, body { width: 875px; height: 1200px; overflow: hidden; }
  body { font-family: 'Ubuntu', sans-serif; color: var(--ink); background: var(--white); position: relative; }

  /* Header */
  .site-header { position: absolute; left: 0; top: 0; width: 875px; height: 88px; background: var(--white); border-bottom: 2px solid var(--orange); }
  .brand { position: absolute; left: 45px; top: 14px; }
  .brand-name { display: flex; align-items: center; gap: 7px; font-size: 22px; font-weight: 700; color: var(--navy); }
  .brand-mark { width: 14px; height: 14px; background: var(--orange); }
  .brand-tagline { margin-top: 8px; font-size: 11px; font-weight: 400; color: var(--ink); letter-spacing: .3px; }
  .lang-select { position: absolute; left: 731px; top: 5px; width: 116px; height: 20px; border: 1px solid #bdbdbd; font-size: 11px; color: #555; padding: 3px 5px; }
  .lang-select::after { content: ""; position: absolute; right: 8px; top: 7px; border: 4px solid transparent; border-top: 6px solid #555; }
  .field { position: absolute; height: 25px; border: 1px solid var(--field-line); border-radius: 2px; font-size: 11px; color: #c2c2c2; padding: 5px 9px; background: var(--white); }
  .field-user { left: 393px; top: 36px; width: 175px; }
  .field-pass { left: 579px; top: 36px; width: 175px; }
  .login-btn { position: absolute; left: 769px; top: 33px; width: 77px; height: 27px; background: var(--login-grey); color: var(--white); border-radius: 2px; font-size: 15px; font-weight: 500; text-align: center; line-height: 27px; }
  .remember { position: absolute; left: 400px; top: 66px; font-size: 11px; color: var(--grey-text); display: flex; align-items: center; gap: 6px; }
  .forgot { position: absolute; left: 579px; top: 66px; font-size: 11px; color: var(--orange); }

  /* Hero */
  .hero { position: absolute; left: 0; top: 89px; width: 875px; height: 532px; overflow: hidden; }
  .hero-photo { position: absolute; inset: 0; background: linear-gradient(100deg, #c6d3df 0%, #d9e1ea 30%, #c3cad3 55%, #e4e9ef 75%, #d1d8e0 100%); }
  .hero-photo::after { content: ""; position: absolute; inset: 0; background: radial-gradient(ellipse at 20% 85%, rgba(90,70,60,.35), transparent 55%), radial-gradient(ellipse at 65% 45%, rgba(180,140,120,.35), transparent 40%); }
  .hero-divider { position: absolute; left: 528px; top: 0; width: 329px; height: 532px; border-left: 1px solid rgba(255,255,255,.7); border-right: 1px solid rgba(255,255,255,.7); }
  .hero-title { position: absolute; left: 28px; top: 48px; font-size: 43px; font-weight: 500; line-height: 51px; color: var(--navy); letter-spacing: .3px; }
  .hero-copy { position: absolute; left: 40px; top: 164px; width: 400px; font-size: 15px; line-height: 26.3px; color: var(--ink); }
  .hero-motto { position: absolute; left: 540px; top: 45px; font-size: 31px; line-height: 31.5px; color: var(--white); font-weight: 400; }
  .signup-box { position: absolute; left: 540px; top: 169px; width: 290px; height: 219px; background: var(--navy-deep); padding: 31px 13px 0; color: var(--white); }
  .signup-lead { font-size: 13px; font-weight: 500; line-height: 15px; }
  .signup-email { margin-top: 19px; height: 32px; background: var(--white); border-radius: 2px; font-size: 11.5px; color: #a5a5a5; padding: 9px 9px; }
  .signup-btn { margin-top: 18px; width: 130px; height: 35px; background: var(--orange); border-radius: 2px; font-size: 14.5px; font-weight: 500; line-height: 35px; padding-left: 18px; }

  /* Partners */
  .partners { position: absolute; left: 0; top: 621px; width: 875px; height: 125px; background: var(--partners-bg); }
  .section-title { text-align: center; font-size: 26px; font-weight: 400; color: #333; }
  .partners .section-title { padding-top: 18px; }
  .partner-row { position: absolute; left: 30px; top: 72px; width: 810px; display: flex; justify-content: space-between; align-items: center; }
  .partner { display: flex; align-items: center; gap: 6px; font-size: 20px; font-weight: 500; color: #4a4a4a; }
  .partner-dot { width: 14px; height: 14px; border-radius: 50%; background: #5a5a5a; }

  /* How it works */
  .how { position: absolute; left: 0; top: 746px; width: 875px; height: 402px; background: var(--how-bg); border-bottom: 2px solid var(--orange); }
  .how .section-title { padding-top: 28px; }
  .video-frame { position: absolute; left: 174px; top: 79px; width: 558px; height: 276px; background: var(--white); border: 1px solid #9eb3c7; box-shadow: 0 0 3px rgba(0,0,0,.2); }
  .video-still { position: absolute; left: 14px; top: 6px; width: 528px; height: 262px; background: linear-gradient(180deg, #ffffff 0%, #ffffff 30%, #c3262d 32%, #a91d23 90%, #ffffff 92%); }
  .player-bar { position: absolute; left: 39px; top: 231px; width: 489px; height: 28px; }
</style>
</head>
<body>

<header class="site-header">
  <div class="brand">
    <div class="brand-name"><span class="brand-mark"></span>StayCrewly.com</div>
    <div class="brand-tagline">a friend for your guests</div>
  </div>
  <div class="lang-select">Choose language</div>
  <div class="field field-user">Username or email</div>
  <div class="field field-pass">Password</div>
  <div class="login-btn">Login</div>
  <div class="remember">
    <svg width="10" height="10" viewBox="0 0 10 10"><rect x=".5" y=".5" width="9" height="9" fill="none" stroke="#777"/><path d="M2 5l2 2 4-5" fill="none" stroke="#444" stroke-width="1.4"/></svg>
    Remember me
  </div>
  <div class="forgot">Forgot password</div>
</header>

<section class="hero">
  <div class="hero-photo" role="img" aria-label="Blurred photo of a team of colleagues giving each other a high five in a bright office"></div>
  <div class="hero-divider"></div>
  <h1 class="hero-title">The Booking<br>Collaboration Platform</h1>
  <p class="hero-copy">Vacation rental managers and hosts can now team up with a booking team. Its easy to instantly improve your online booking management. Be on all the best booking sites without all the hassle. Improve your current strategy and save loads of time which you can spend on the satisfaction of your guests.</p>
  <div class="hero-motto">TEAM UP<br>SHARE<br>DO BETTER</div>
  <div class="signup-box">
    <p class="signup-lead">Join the free booking network with optional personal booking team today</p>
    <div class="signup-email">Enter email</div>
    <div class="signup-btn">Register</div>
  </div>
</section>

<section class="partners">
  <h2 class="section-title">Our partners</h2>
  <div class="partner-row">
    <div class="partner"><span class="partner-dot"></span>Roamvale</div>
    <div class="partner"><span class="partner-dot"></span>Lodgeburg</div>
    <div class="partner"><span class="partner-dot"></span>Keyfinch</div>
    <div class="partner">Tripmoor</div>
    <div class="partner"><span class="partner-dot"></span>Bunkhaven</div>
    <div class="partner">Staylark.com</div>
  </div>
</section>

<section class="how">
  <h2 class="section-title">How it works</h2>
  <div class="video-frame">
    <div class="video-still" role="img" aria-label="Explainer video still: step one, share bookings and services on the social platform, with a red card of greetings in many languages"></div>
    <svg class="player-bar" viewBox="0 0 489 28" width="489" height="28">
      <rect x="0" y="0" width="489" height="28" fill="#e4e4e4" stroke="#c9c9c9"/>
      <path d="M13 8l12 6-12 6z" fill="#444"/>
      <line x1="36" y1="5" x2="36" y2="23" stroke="#c0c0c0"/>
      <rect x="44" y="10" width="245" height="8" rx="4" fill="#5e5e5e"/>
      <rect x="44" y="10" width="120" height="8" rx="4" fill="#e8434a"/>
      <circle cx="164" cy="14" r="5" fill="#f4f4f4" stroke="#888"/>
      <text x="297" y="18" font-family="Ubuntu, sans-serif" font-size="9.5" fill="#333">3.47 / 9.29</text>
      <line x1="353" y1="5" x2="353" y2="23" stroke="#c0c0c0"/>
      <path d="M362 11h4l5-4v14l-5-4h-4z" fill="#555"/>
      <rect x="383" y="10" width="66" height="8" rx="4" fill="#5e5e5e"/>
      <circle cx="445" cy="14" r="4" fill="#f4f4f4" stroke="#888"/>
      <line x1="459" y1="5" x2="459" y2="23" stroke="#c0c0c0"/>
      <rect x="469" y="8" width="12" height="12" fill="none" stroke="#555" stroke-width="1.5"/>
      <rect x="472" y="11" width="6" height="6" fill="#555"/>
    </svg>
  </div>
</section>

<footer class="site-footer" style="position:absolute;left:0;top:1150px;width:875px;height:50px;background:var(--footer-bg);display:flex;justify-content:center;align-items:center;gap:12px;font-size:11px;color:var(--white);">
  <span>Terms and conditions</span><span>|</span><span>Contact us</span><span>|</span><span>About us</span>
</footer>

</body>
</html>
```